card design for engineering consultancy

engineering drafting and project management company the provides drafting services for.
Electrical, Hydraulic, Mechanical, and Civil services
The company is called K7R Services and logo is as attached
Information on card should be.
1. Logo
2.website : K7RServices.com
3. email : info@K7RServices.com
4. Phone: (+61) 400512738
5. Motto: Design - Document - Develop - Deliver

this card should be basically used for business identification only

Target Market(s)

electricians plumbers air conditioning installers and civil contractors

Industry/Entity Type

engineering, drafting, electrical, plumbing, airconditioning, civil

Contact Information for Business Card

1. Logo 2.website : K7RServices.com 3. email : info@K7RServices.com 4. Phone: (+61) 400512738 5. Motto: Design - Document - Develop - Deliver

Font styles to use
Serif

Requirements
Must have
• logo
Nice to have
• something inovative and different that makes it stand out from being just another business card

```html
<!DOCTYPE html>
<html lang="en">
<head>
<meta charset="utf-8">
<title>K7R Services – Business Card</title>
<link rel="stylesheet" href="https://fonts.googleapis.com/css2?family=Nunito+Sans:wght@400;700;800&display=swap">
<style>
  :root {
    --backdrop: #d9d9d9;
    --card: #0d0d0d;
    --frame: #a3a3a3;
    --brand-grey: #545050;
    --brand-red: #cc1b24;
    --contact-text: #a9a9a9;
    --rule: #5a5a5a;
  }
  * { margin: 0; padding: 0; box-sizing: border-box; }
  html, body { width: 1200px; height: 900px; overflow: hidden; }
  body {
    background: var(--backdrop);
    font-family: "Nunito Sans", Arial, sans-serif;
    position: relative;
  }
  .card {
    position: absolute;
    left: 237px;
    width: 685px;
    height: 392px;
    background: var(--card);
    box-shadow: 0 3px 10px rgba(0,0,0,0.35);
  }
  .card--front { top: 43px; }
  .card--back { top: 465px; }
  .card__frame {
    position: absolute;
    inset: 7px;
    border: 2px solid var(--frame);
  }
  .brand-name {
    position: absolute;
    left: 0; right: 0;
    display: flex;
    justify-content: center;
    align-items: center;
    gap: 18px;
    color: var(--brand-grey);
    font-weight: 800;
    text-transform: uppercase;
    letter-spacing: 0.08em;
    white-space: nowrap;
  }
  .brand-name__square {
    background: var(--brand-red);
    flex: none;
  }
  .card--front .brand-name { top: 158px; font-size: 60px; }
  .card--front .brand-name__square { width: 44px; height: 44px; }
  .card--back .brand-name { top: 110px; font-size: 42px; gap: 14px; }
  .card--back .brand-name__square { width: 30px; height: 30px; }
  .motto {
    position: absolute;
    top: 254px;
    left: 0; right: 0;
    text-align: center;
    color: var(--brand-red);
    font-size: 25px;
    font-weight: 400;
    letter-spacing: 0.42em;
    white-space: nowrap;
    padding-left: 16px;
  }
  .card__rule {
    position: absolute;
    top: 303px;
    left: 17px;
    right: 18px;
    height: 1px;
    background: var(--rule);
  }
  .contact-list {
    position: absolute;
    top: 327px;
    left: 58px;
    display: flex;
    gap: 24px;
    list-style: none;
    color: var(--contact-text);
    font-size: 14.5px;
    letter-spacing: 0.06em;
    white-space: nowrap;
  }
  .contact-list__item { display: flex; align-items: center; gap: 8px; }
  .contact-list__icon { width: 16px; height: 16px; fill: var(--brand-red); flex: none; }
</style>
</head>
<body>
  <section class="card card--front">
    <div class="card__frame"></div>
    <div class="brand-name"><span class="brand-name__square"></span>K7R Services</div>
  </section>

  <section class="card card--back">
    <div class="card__frame"></div>
    <div class="brand-name"><span class="brand-name__square"></span>K7R Services</div>
    <p class="motto">Document - Develop - Deliver</p>
    <div class="card__rule"></div>
    <ul class="contact-list">
      <li class="contact-list__item">
        <svg class="contact-list__icon" viewBox="0 0 24 24" aria-hidden="true"><path d="M6.6 10.8a15.1 15.1 0 0 0 6.6 6.6l2.2-2.2a1 1 0 0 1 1-.25 11.4 11.4 0 0 0 3.6.57 1 1 0 0 1 1 1V20a1 1 0 0 1-1 1A17 17 0 0 1 3 4a1 1 0 0 1 1-1h3.5a1 1 0 0 1 1 1c0 1.25.2 2.45.57 3.57a1 1 0 0 1-.25 1z"/></svg>
        (+61) 400512738
      </li>
      <li class="contact-list__item">
        <svg class="contact-list__icon" viewBox="0 0 24 24" aria-hidden="true"><path d="M2 5h20v14H2z M2 5l10 8 10-8" fill="var(--brand-red)" stroke="var(--card)" stroke-width="1.6"/></svg>
        info@K7RServices.com
      </li>
      <li class="contact-list__item">
        <svg class="contact-list__icon" viewBox="0 0 24 24" aria-hidden="true" fill="none" stroke="var(--brand-red)" stroke-width="1.6"><circle cx="12" cy="12" r="9.5"/><ellipse cx="12" cy="12" rx="4" ry="9.5"/><path d="M2.5 12h19M4 7h16M4 17h16"/></svg>
        K7RServices.com
      </li>
    </ul>
  </section>
</body>
</html>
```